Business Card for: Northbrook Financial Advisory Services Inc.

provide strategic financial advisory services to companies in the areas of corporate finance, mergers and acquisitions, executive coaching and strategic planning

Target Market(s)

Companies, banks, accountants, lawyers

Industry/Entity Type

High end business consulting in corporate finance, mergers and acquisitions, consulting

Contact Information for Business Card

Name of company, Name: xxxxxx xxxxxx , CEO, - phone number: 1-xxx-xxx-xxxx, - email address,

Requirements
Must have
• Must be professional and simple.
Nice to have
• simple, straight graphics, must give the impression that we are trustworthy, professional, competent
Should not have
• loud colors, loud design features

```html
<!DOCTYPE html>
<html lang="en">
<head>
<meta charset="utf-8">
<title>Northbrook Financial Advisory Inc – Business Card</title>
<link href="https://fonts.googleapis.com/css2?family=Montserrat:wght@400;500&family=Open+Sans:wght@400;600&display=swap" rel="stylesheet">
<style>
  :root {
    --backdrop: #a6a6a6;
    --card-white: #ffffff;
    --card-black: #0d0d0d;
    --pattern-tone: #1c1c1c;
    --brand-red: #c01c24;
    --rule-grey: #e1e1e1;
    --ink: #1a1a1a;
    --ink-soft: #444444;
    --divider: #9a9a9a;
  }
  * { margin: 0; padding: 0; box-sizing: border-box; }
  html, body { width: 900px; height: 1200px; overflow: hidden; }
  body {
    background: var(--backdrop);
    font-family: "Open Sans", Arial, sans-serif;
    position: relative;
  }
  .card {
    position: absolute;
    left: 190px;
    width: 520px;
    height: 298px;
    overflow: hidden;
    box-shadow: 0 6px 14px rgba(0,0,0,.28);
  }

  /* Front */
  .card--front { top: 277px; background: var(--card-black); }
  .front-texture {
    position: absolute; inset: 0 0 29px 0;
    background: radial-gradient(ellipse at 50% 45%, var(--pattern-tone) 0%, var(--card-black) 75%);
  }
  .front-brand {
    position: absolute; left: 0; right: 0; top: 96px;
    text-align: center; color: var(--card-white);
    font-family: "Montserrat", Arial, sans-serif; font-weight: 400;
  }
  .front-brand__name { font-size: 27px; letter-spacing: .5px; line-height: 1.1; }
  .front-brand__line { font-size: 15px; letter-spacing: .4px; margin-top: 3px; }
  .front-services {
    position: absolute; left: 0; right: 0; top: 174px;
    display: flex; justify-content: center;
    color: var(--card-white); font-size: 9.5px;
  }
  .front-services span { padding: 0 6px; border-left: 1.5px solid var(--brand-red); line-height: 14px; }
  .front-services span:first-child { border-left: none; }
  .front-band {
    position: absolute; left: 0; right: 0; bottom: 0; height: 29px;
    background: var(--brand-red); color: var(--card-white);
    font-size: 8.5px; letter-spacing: 2.6px;
    display: flex; align-items: center; justify-content: center;
  }

  /* Back */
  .card--back { top: 625px; background: var(--card-white); }
  .back-stripe { position: absolute; left: 280px; width: 20px; }
  .back-stripe--top { top: 0; height: 92px; background: var(--brand-red); }
  .back-stripe--mid { top: 98px; height: 119px; background: var(--rule-grey); }
  .back-stripe--bottom { top: 230px; height: 68px; background: var(--brand-red); }
  .back-company {
    position: absolute; left: 30px; top: 103px;
    font-family: "Montserrat", Arial, sans-serif; font-weight: 400;
    font-size: 17px; line-height: 22px; color: var(--ink);
  }
  .back-company__rule {
    position: absolute; left: 0; top: 148px; width: 254px; height: 1.5px;
    background: var(--brand-red);
  }
  .back-services {
    position: absolute; left: 30px; top: 174px;
    display: grid; grid-template-columns: 120px 1px 130px; column-gap: 15px;
    font-size: 9px; color: var(--ink-soft); line-height: 19px;
  }
  .back-services__divider { background: var(--divider); height: 36px; margin-top: 2px; }
  .back-person { position: absolute; left: 327px; top: 114px; color: var(--ink); }
  .back-person__name { font-family: "Montserrat", Arial, sans-serif; font-size: 14px; letter-spacing: .6px; }
  .back-person__role { font-size: 10px; color: var(--ink-soft); margin-top: 1px; }
  .back-contacts { position: absolute; left: 327px; top: 168px; list-style: none; }
  .back-contacts li {
    display: flex; align-items: center; gap: 9px;
    font-size: 11px; color: var(--ink); height: 19px;
  }
  .contact-icon { width: 13px; height: 13px; display: block; }
</style>
</head>
<body>

  <section class="card card--front" aria-label="Business card front">
    <div class="front-texture" role="img" aria-label="Subtle dark triangle pattern background"></div>
    <div class="front-brand">
      <div class="front-brand__name">NORTHBROOK</div>
      <div class="front-brand__line">Financial Advisory Inc</div>
    </div>
    <div class="front-services">
      <span>Corporate finance</span>
      <span>Mergers and Acquisitions</span>
      <span>Executive Coaching</span>
      <span>Strategic Planning</span>
    </div>
    <div class="front-band">www.mywebsite.com</div>
  </section>

  <section class="card card--back" aria-label="Business card back">
    <div class="back-stripe back-stripe--top"></div>
    <div class="back-stripe back-stripe--mid"></div>
    <div class="back-stripe back-stripe--bottom"></div>

    <div class="back-company">Northbrook<br>Financial Advisory Inc</div>
    <div class="back-company__rule"></div>

    <div class="back-services">
      <div>Corporate finance<br>Mergers and Acquisitions</div>
      <div class="back-services__divider"></div>
      <div>Executive Coaching<br>Strategic Planning</div>
    </div>

    <div class="back-person">
      <div class="back-person__name">LOREM IPSUM</div>
      <div class="back-person__role">Director</div>
    </div>

    <ul class="back-contacts">
      <li>
        <svg class="contact-icon" viewBox="0 0 13 13" aria-hidden="true">
          <rect width="13" height="13" fill="#c01c24"/>
          <path d="M3.6 2.8 L5.2 2.8 L5.8 4.8 L4.9 5.6 Q5.8 7.4 7.5 8.2 L8.3 7.3 L10.2 7.9 L10.2 9.5 Q9.8 10.3 8.8 10.2 Q3.2 9.2 2.8 3.8 Q2.8 3 3.6 2.8 Z" fill="#fff"/>
        </svg>
        123 1234 123
      </li>
      <li>
        <svg class="contact-icon" viewBox="0 0 13 13" aria-hidden="true">
          <rect width="13" height="13" fill="#c01c24"/>
          <rect x="2.5" y="3.8" width="8" height="5.6" fill="#fff"/>
          <path d="M2.5 3.8 L6.5 7 L10.5 3.8" fill="none" stroke="#c01c24" stroke-width=".9"/>
        </svg>
        my company@mail.com
      </li>
      <li>
        <svg class="contact-icon" viewBox="0 0 13 13" aria-hidden="true">
          <rect width="13" height="13" fill="#c01c24"/>
          <circle cx="6.5" cy="6.5" r="3.8" fill="none" stroke="#fff" stroke-width="1"/>
          <ellipse cx="6.5" cy="6.5" rx="1.6" ry="3.8" fill="none" stroke="#fff" stroke-width=".8"/>
          <line x1="2.7" y1="6.5" x2="10.3" y2="6.5" stroke="#fff" stroke-width=".8"/>
        </svg>
        www.mywebsite.com
      </li>
    </ul>
  </section>

</body>
</html>
```